Brochure for property management company
Cedarfield Realty Associates
Managing Your Investment With Care
Real Estate
Condominium and Homeowner Associations
Current Brochure Design (Outside)
Current Brochure Design (Inside) NEED NEW LOOK
vector logo file

```html
<!DOCTYPE html>
<html lang="en">
<head>
<meta charset="utf-8">
<title>Cedarfield Realty Associates – Brochure Outside</title>
<link href="https://fonts.googleapis.com/css2?family=Arimo:wght@400;700&display=swap" rel="stylesheet">
<style>
  :root {
    --navy: #16306b;
    --blue: #1f56a8;
    --sky: #3b7fd0;
    --white: #ffffff;
    --paper: #f4f5f7;
    --ink: #1b2a4a;
    --stage: #e6e7ea;
  }
  * { box-sizing: border-box; margin: 0; padding: 0; }
  html, body { width: 1200px; height: 552px; overflow: hidden; }
  body { background: var(--stage); font-family: "Arimo", Arial, sans-serif; color: var(--ink); }
  .spread {
    position: absolute; left: 30px; top: 16px; width: 1140px; height: 520px;
    display: flex; background: var(--white);
    box-shadow: 0 2px 10px rgba(0,0,0,.18);
  }
  .panel { position: relative; width: 380px; height: 520px; overflow: hidden; }

  /* Left panel: services */
  .services { background: var(--blue); color: var(--white); }
  .services-box { position: absolute; left: 0; top: 0; width: 330px; height: 320px; padding: 18px 20px; background: var(--navy); }
  .services h2 { font-size: 17px; font-weight: 700; margin-bottom: 8px; }
  .services p { font-size: 11px; line-height: 1.45; margin-bottom: 14px; }
  .services h3 { font-size: 13px; font-weight: 700; line-height: 1.3; margin-bottom: 8px; }
  .services ul { list-style: none; font-size: 11px; line-height: 1.6; }
  .services li::before { content: "\2022"; margin-right: 6px; }
  .services-strip { position: absolute; right: 0; top: 0; width: 50px; height: 520px; background: var(--sky); }
  .photo-crew { position: absolute; left: 14px; top: 336px; width: 150px; height: 90px; background: linear-gradient(135deg, #9bb4cf, #c9b48a); }
  .photo-towers { position: absolute; left: 14px; top: 434px; width: 150px; height: 76px; background: linear-gradient(180deg, #6f9fd6, #2b4f86); }
  .photo-office { position: absolute; left: 172px; top: 336px; width: 150px; height: 90px; background: linear-gradient(135deg, #b9c7d6, #7d8fa6); }

  /* Middle panel: back cover with contacts */
  .contact { background: var(--white); }
  .contact-band { position: absolute; left: 0; top: 0; width: 44px; height: 520px; background: var(--blue); }
  .photo-team { position: absolute; left: 54px; top: 26px; width: 300px; height: 200px; background: linear-gradient(180deg, #cdd8e6, #5d6e86); }
  .brand { font-family: "Arimo", Arial, sans-serif; font-weight: 700; color: var(--navy); }
  .contact .brand { position: absolute; left: 64px; top: 250px; width: 290px; font-size: 22px; line-height: 1.15; }
  .contact-info { position: absolute; left: 54px; top: 330px; width: 316px; height: 120px; padding: 14px 16px; background: var(--navy); color: var(--white); font-size: 11px; line-height: 1.55; }
  .contact-info strong { font-size: 12px; }
  .web { font-size: 13px; font-weight: 700; color: var(--navy); }
  .contact .web { position: absolute; left: 64px; top: 478px; }

  /* Right panel: front cover */
  .cover { background: var(--white); }
  .cover-strip { position: absolute; right: 0; top: 0; width: 36px; height: 520px; background: var(--navy); }
  .cover .brand { position: absolute; left: 30px; top: 22px; width: 300px; font-size: 24px; line-height: 1.15; display: flex; align-items: center; gap: 10px; }
  .brand-square { width: 18px; height: 18px; background: var(--navy); flex: none; }
  .photo-cover { position: absolute; left: 20px; top: 100px; width: 324px; height: 220px; background: linear-gradient(180deg, #a9c6e4, #dfe6ea 55%, #6b7a8c); }
  .tagline { position: absolute; left: 30px; top: 346px; width: 310px; color: var(--navy); font-weight: 700; text-align: right; }
  .tagline .t1 { font-size: 24px; display: block; }
  .tagline .t2 { font-size: 34px; display: block; line-height: 1.1; }
  .tagline .t3 { font-size: 20px; font-weight: 400; display: block; }
  .cover-band { position: absolute; left: 0; bottom: 0; width: 344px; height: 44px; background: var(--blue); }
  .cover .web { position: absolute; right: 50px; bottom: 14px; color: var(--white); }
</style>
</head>
<body>
<div class="spread">
  <section class="panel services">
    <div class="services-strip"></div>
    <div class="services-box">
      <h2>Our Services:</h2>
      <p>TCRA has the resources, experience and depth of knowledge to offer the following services to condominium, homeowner associations &amp; cooperatives. We tailor each plan to your community's needs and budget.</p>
      <h3>Our Services include but are not limited to:</h3>
      <ul>
        <li>Residential Management</li>
        <li>Complete Financial Reporting</li>
        <li>Construction Management</li>
        <li>Preventive Project Management</li>
        <li>On-Site Maintenance</li>
        <li>Insurance</li>
        <li>24 Hour Emergency Service</li>
      </ul>
    </div>
    <div class="photo-crew" role="img" aria-label="Photo of a maintenance crew at work"></div>
    <div class="photo-office" role="img" aria-label="Photo of staff meeting with clients"></div>
    <div class="photo-towers" role="img" aria-label="Photo of high-rise residential towers"></div>
  </section>

  <section class="panel contact">
    <div class="contact-band"></div>
    <div class="photo-team" role="img" aria-label="Photo of the management team in business suits"></div>
    <div class="brand">Cedarfield Realty Associates</div>
    <div class="contact-info">
      <strong>Cedarfield Realty Associates, Inc.</strong><br>
      48 Larchmont Way, Suite 12<br>
      Brookhaven, GA 30519<br>
      Phone: (404) 555-0182<br>
      Email: info@cedarfield-realty.net
    </div>
    <div class="web">www.cedarfield-realty.net</div>
  </section>

  <section class="panel cover">
    <div class="cover-strip"></div>
    <div class="brand"><span class="brand-square"></span>Cedarfield Realty Associates</div>
    <div class="photo-cover" role="img" aria-label="Photo of a property manager standing before a residential building"></div>
    <h1 class="tagline">
      <span class="t1">Managing Your</span>
      <span class="t2">Investment</span>
      <span class="t3">With Care</span>
    </h1>
    <div class="cover-band"></div>
    <div class="web">www.cedarfield-realty.net</div>
  </section>
</div>
</body>
</html>
```